Brake Test Training for Coal Mining

We offer Brake Test Training for Coal Mine workers. It's a legislative requirement that workers who are tasked with performing brake testing have certain competencies to do so. We test Light Vehicles and trailers, Heavy Vehicles and Mobile Mining Equipment like Graders, Scrapers and Dump Trucks.

```html
<!DOCTYPE html>
<html lang="en">
<head>
<meta charset="utf-8">
<title>Brake Test Training for Coal Mining</title>
<link rel="stylesheet" href="https://fonts.googleapis.com/css2?family=Archivo:wght@600;700;800;900&display=swap">
<style>
  :root {
    --navy: #27387c;
    --navy-deep: #1f2d6a;
    --navy-band: #223171;
    --yellow: #ffcc00;
    --white: #ffffff;
    --ink: #0b0b0b;
    --link-ink: #1c2a66;
  }
  * { margin: 0; padding: 0; box-sizing: border-box; }
  html, body { width: 1200px; height: 588px; overflow: hidden; background: var(--navy); }
  .banner {
    position: relative; width: 1200px; height: 588px; overflow: hidden;
    font-family: "Archivo", Arial, sans-serif; color: var(--white);
  }
  .backdrop {
    position: absolute; inset: 0 0 156px 0;
    background:
      radial-gradient(ellipse 260px 220px at 720px 190px, rgba(120,130,190,0.45), transparent 70%),
      linear-gradient(180deg, #2b3d84 0%, #2a3a80 55%, #34498e 100%);
  }
  .truck-photo {
    position: absolute; left: 782px; top: 18px; width: 418px; height: 414px;
    background:
      radial-gradient(circle at 62% 22%, rgba(255,230,170,0.9), transparent 18%),
      linear-gradient(160deg, #c98a2d 0%, #a8611c 45%, #6b4a2e 70%, #4a4a4f 100%);
    clip-path: polygon(42% 0, 100% 0, 100% 100%, 0 100%, 0 60%, 14% 45%, 30% 22%);
  }
  .brand {
    position: absolute; left: 91px; top: 50px; display: flex; align-items: center; gap: 16px;
  }
  .brand-mark { width: 62px; height: 62px; border-radius: 50%; border: 4px solid var(--white); }
  .brand-name {
    font-weight: 800; font-size: 24px; line-height: 1.15; letter-spacing: 1px;
    text-transform: uppercase; color: var(--white);
  }
  .web-strip {
    position: absolute; left: 410px; top: 52px; width: 420px; height: 66px;
    background: linear-gradient(90deg, var(--yellow) 0%, var(--yellow) 70%, rgba(255,204,0,0) 100%);
    display: flex; align-items: center; padding-left: 15px; gap: 12px;
    color: var(--link-ink); font-weight: 800; font-size: 31px; letter-spacing: -0.5px;
  }
  .headline {
    position: absolute; left: 74px; top: 146px;
    font-weight: 900; font-size: 84px; line-height: 71px; letter-spacing: -3px;
    text-transform: uppercase;
  }
  .headline .accent { color: var(--yellow); display: block; }
  .intro {
    position: absolute; left: 91px; top: 312px; width: 740px;
    font-weight: 700; font-size: 21px; line-height: 30px; letter-spacing: -0.6px;
    text-transform: uppercase;
  }
  .contact-band {
    position: absolute; left: 0; top: 432px; width: 1200px; height: 156px; background: var(--navy-band);
  }
  .phone {
    position: absolute; left: 48px; top: 469px; display: flex; align-items: center; gap: 28px;
  }
  .phone-icon { width: 80px; height: 80px; }
  .phone-number {
    font-weight: 800; font-size: 82px; letter-spacing: -3px; line-height: 1; color: var(--white);
  }
  .apply {
    position: absolute; left: 694px; top: 432px; width: 506px; height: 156px;
    background: var(--yellow); clip-path: polygon(53px 0, 100% 0, 100% 100%, 0 100%);
    display: flex; align-items: center; justify-content: flex-end; padding-right: 58px;
    font-weight: 900; font-size: 62px; letter-spacing: -2px; color: var(--ink); text-transform: uppercase;
  }
</style>
</head>
<body>
<main class="banner">
  <div class="backdrop" role="img" aria-label="Dusk city skyline with a mine worker in a hard hat"></div>
  <div class="truck-photo" role="img" aria-label="Orange heavy haulage truck, front view with headlights on"></div>

  <div class="brand">
    <span class="brand-mark"></span>
    <span class="brand-name">Southern<br>Plant Training</span>
  </div>

  <div class="web-strip">
    <svg width="40" height="40" viewBox="0 0 40 40" fill="none" stroke="#1c2a66" stroke-width="3">
      <circle cx="20" cy="20" r="17"/>
      <ellipse cx="20" cy="20" rx="8" ry="17"/>
      <line x1="3" y1="20" x2="37" y2="20"/>
      <line x1="6" y1="11" x2="34" y2="11"/>
      <line x1="6" y1="29" x2="34" y2="29"/>
    </svg>
    <span>www.spt-train.com.au</span>
  </div>

  <h1 class="headline">Your Trusted<span class="accent">Training Partner</span></h1>

  <p class="intro">We offer brake test training for coal mine workers. We test light vehicles and trailers, heavy vehicles and mobile mining equipment like graders, scrapers and dump trucks.</p>

  <div class="contact-band"></div>
  <div class="phone">
    <svg class="phone-icon" viewBox="0 0 80 80">
      <circle cx="40" cy="40" r="40" fill="#ffcc00"/>
      <path d="M30 22c2-1 4 0 5 2l3 7c1 2 0 4-1 5l-3 2c2 5 6 9 11 11l2-3c1-1 3-2 5-1l7 3c2 1 3 3 2 5l-2 5c-1 2-3 3-5 3-15-1-28-14-29-29 0-2 1-4 3-5z" fill="#223171"/>
    </svg>
    <span class="phone-number">1300 555 018</span>
  </div>
  <div class="apply">Apply Now</div>
</main>
</body>
</html>
```